Pawsome Trails business card

I need a business card design for a dog training company in Toronto called Pawsome Trails. My training is unique, outdoor training that helps people create a better bond with their dog through communication and understanding their dog's true nature. I do not use treats - but communication and praise for the dog.

I help people create a better life for them and their dog. From puppy training right through to seniors, I offer both group classes called Curbside Calm Program as well as in-home private sessions.

I believe that having a dog is a lifestyle, so I encourage clients to incorporate their dog into their active life. Outdoor activities such as hiking, mental stimulation, proper care and healthy food for their dog are all keys to a healthy and happy dog.

I would like a fresh and modern look that works with my logo. I would like to convey fun, confidence and happiness.

My services are premium services. I am a Certified Dog Trainer, and offer value for money, but my prices are higher than other trainers.
Updates

Thank you to everyone who submitted designs! I'm so impressed with the level of creativity and the options that you all have given me. It will be a difficult choice for sure. As this was my first experience with Sketch Bazaar - it has been a great one.

marla.

Industry/Entity Type

Communication

Requirements
Must have
• Marla Quinby, CTE
Certified Trainer Educator
marla@pawsometrails.ca
647-555-0183
pawsometrails.ca

Prefer a double sided card.
Must have Pawsome Trails logo. File attached. I do have a stroke logo for a dark background as well.

Must only use the fonts and colours as outlined in my brand guidelines, which are attached.
Should not have
• no cheesy pet images
do not use the tongue as an element outside of the logo
minimize the use of pink - can be used as an accent colour but should not be a main colour

```html
<!DOCTYPE html>
<html lang="en">
<head>
<meta charset="utf-8">
<title>Pawsome Trails business card</title>
<link rel="stylesheet" href="https://fonts.googleapis.com/css2?family=Source+Sans+3:wght@300;400;600;700&display=swap">
<style>
  :root {
    --bg: #e9e7e4;
    --charcoal: #3b3b3d;
    --charcoal-deep: #2f2f31;
    --blue: #1a9fd3;
    --blue-deep: #0d7fb3;
    --green: #8cb33e;
    --pink: #e77fb6;
    --white: #ffffff;
    --grey-text: #6d6d6f;
    --paper: #f6f6f6;
  }
  * { box-sizing: border-box; margin: 0; padding: 0; }
  html, body {
    width: 1200px; height: 923px; overflow: hidden;
    background: var(--bg);
    font-family: "Source Sans 3", sans-serif;
  }
  .sheet {
    width: 1200px; height: 923px;
    display: flex; flex-direction: column; align-items: center; justify-content: center; gap: 44px;
  }
  .card {
    position: relative; width: 720px; height: 411px;
    border-radius: 22px; overflow: hidden;
    box-shadow: 0 10px 28px rgba(0,0,0,.18);
  }
  .card__waves { position: absolute; inset: 0; width: 100%; height: 100%; }
  .card--front { background: linear-gradient(160deg, var(--charcoal) 0%, var(--charcoal-deep) 100%); }
  .card--back { background: linear-gradient(160deg, var(--white) 0%, var(--paper) 100%); }

  .brand-name {
    position: absolute;
    font-weight: 700; line-height: 1; letter-spacing: -0.5px;
    color: var(--green); white-space: nowrap;
  }
  .card--front .brand-name { left: 70px; top: 176px; font-size: 46px; }
  .card--back .brand-name { left: 56px; top: 262px; font-size: 40px; }

  .front-web {
    position: absolute; right: 48px; top: 188px;
    color: var(--white); font-weight: 400; font-size: 19px; letter-spacing: 3px;
  }

  .identity { position: absolute; left: 300px; top: 30px; }
  .identity__name { font-weight: 600; font-size: 34px; color: var(--blue); line-height: 1; }
  .identity__creds { font-weight: 400; font-size: 15px; color: var(--grey-text); margin-left: 4px; }
  .identity__title { font-weight: 300; font-size: 17px; color: var(--grey-text); margin-top: 8px; letter-spacing: .3px; }

  .contact {
    position: absolute; right: 34px; top: 228px;
    text-align: right; color: var(--white);
    font-style: normal; font-weight: 400; font-size: 15px; line-height: 1.5;
  }
  .contact__web { font-size: 18px; letter-spacing: 3px; margin-top: 4px; }
</style>
</head>
<body>
<main class="sheet">
  <section class="card card--front" aria-label="Card front">
    <svg class="card__waves" viewBox="0 0 720 411" preserveAspectRatio="none" aria-hidden="true">
      <defs>
        <linearGradient id="frontBlue" x1="0" y1="0" x2="1" y2="1">
          <stop offset="0" stop-color="#23aee0"/>
          <stop offset="1" stop-color="#0d7fb3"/>
        </linearGradient>
      </defs>
      <path d="M455,0 C600,110 330,330 205,411 L720,411 L720,0 Z" fill="var(--pink)"/>
      <path d="M468,0 C615,110 345,330 222,411 L720,411 L720,0 Z" fill="var(--charcoal)"/>
      <path d="M476,0 C625,110 355,330 234,411 L720,411 L720,0 Z" fill="var(--green)"/>
      <path d="M492,0 C640,110 372,330 254,411 L720,411 L720,0 Z" fill="var(--blue-deep)"/>
      <path d="M500,0 C650,110 382,330 266,411 L720,411 L720,0 Z" fill="url(#frontBlue)"/>
    </svg>
    <p class="brand-name">Pawsome Trails</p>
    <p class="front-web">www.pawsometrails.ca</p>
  </section>

  <section class="card card--back" aria-label="Card back">
    <svg class="card__waves" viewBox="0 0 720 411" preserveAspectRatio="none" aria-hidden="true">
      <defs>
        <linearGradient id="backBlue" x1="0" y1="0" x2="1" y2="1">
          <stop offset="0" stop-color="#23aee0"/>
          <stop offset="1" stop-color="#0d7fb3"/>
        </linearGradient>
      </defs>
      <path d="M720,60 C540,60 390,190 300,411 L720,411 Z" fill="var(--charcoal)"/>
      <path d="M720,65 C554,65 404,190 314,411 L720,411 Z" fill="var(--white)"/>
      <path d="M720,68 C562,68 412,190 322,411 L720,411 Z" fill="var(--green)"/>
      <path d="M720,74 C580,74 430,190 340,411 L720,411 Z" fill="var(--blue-deep)"/>
      <path d="M720,78 C590,78 440,190 350,411 L720,411 Z" fill="url(#backBlue)"/>
    </svg>
    <div class="identity">
      <p class="identity__name">Marla Quinby <span class="identity__creds">CTE</span></p>
      <p class="identity__title">Certified Trainer Educator</p>
    </div>
    <p class="brand-name">Pawsome Trails</p>
    <address class="contact">
      <p>P: 647-555-0183</p>
      <p>E: marla@pawsometrails.ca</p>
      <p>#1321, Your Street, Your Location</p>
      <p>Your Town, Your Country</p>
      <p class="contact__web">www.pawsometrails.ca</p>
    </address>
  </section>
</main>
</body>
</html>
```